Report layout - design layout for automatic welcome letter PDF

We need to design the layout for a welcome letter PDF being automatically generated by an Enterprise web application.
We give you the ugly Ms. Word layout, we need to create a nice template for the same content to be automatically generated in PDF.
In particular we attached:
Reason: Hi guys,
I was unfortunately sick in the last few days and I could not work on the designs feedback. Now I am back, please apologize.
I am extending the deadline of 5 days in order to sort things out.
I want to thank you guys already for nice design received!
Teodoro
Target Market(s)
Enterprise business.
Industry/Entity Type
Bank
Requirements
Must have
- 1) Front page with customer details;
- 2) Second page: legal notice.
- If it turns out that we do not fit in 2 pages we can even make 3, but I would keep legal notice separated from customer details.
Nice to have
- 1) Header and footer that makes it easy to create it automatically using PDF.
- 2) You will see that logo and application are using different types of red. I believe we can uniform them. If you have inspiration regarding the logo feel free to suggest.

```html
<!DOCTYPE html>
<html lang="it">
<head>
<meta charset="utf-8">
<title>Modulo di attivazione - LoomStoreVault</title>
<link rel="stylesheet" href="https://fonts.googleapis.com/css2?family=Questrial&family=Open+Sans:wght@400;700&display=swap">
<style>
  :root{
    --red:#e3161d;
    --wine:#7a0f1f;
    --bar:#5c2a2d;
    --box:#b5a0a0;
    --box-text:#ffffff;
    --ink:#1e1e1e;
    --green:#3a9a3a;
    --paper:#ffffff;
  }
  *{margin:0;padding:0;box-sizing:border-box}
  html,body{width:927px;height:1200px;overflow:hidden;background:var(--paper)}
  body{font-family:"Questrial",sans-serif;color:var(--ink);position:relative}
  .corner{position:absolute;left:0;top:0}
  .brand{position:absolute;right:72px;top:46px;text-align:right}
  .brand-name{font-size:27px;letter-spacing:-0.3px;color:var(--ink);line-height:1}
  .brand-url{font-size:17px;color:var(--red);margin-top:2px}
  .partner{position:absolute;right:74px;top:104px;display:flex;align-items:center;gap:8px;font-size:22px;color:var(--ink)}
  .partner-dot{width:24px;height:24px;border-radius:50%;background:var(--green)}
  .title-bar{position:absolute;left:61px;top:228px;width:799px;height:42px;border-radius:14px;background:var(--bar);color:#fff;font-size:20px;padding:9px 12px;letter-spacing:0.2px}
  .text{position:absolute;font-size:19px;line-height:25px;white-space:nowrap}
  .box{position:absolute;left:61px;width:799px;background:var(--box);color:var(--box-text);border-radius:16px;font-size:19.5px;line-height:25px;padding:7px 10px;white-space:nowrap}
  .users{display:flex}
  .users span:nth-child(1){width:212px}
  .users span:nth-child(2){width:294px}
  .sign{display:flex;padding:10px 15px}
  .sign .col{width:410px}
  .sign strong{font-family:"Open Sans",sans-serif;font-weight:700;font-size:19px}
  .line{display:inline-block;border-bottom:1px solid #fff;width:162px;height:16px}
  .footer-rule{position:absolute;left:76px;top:1132px;width:812px;border-top:1px solid #555}
  .footer{position:absolute;left:87px;top:1136px;width:742px;height:58px;display:flex;align-items:center;font-family:"Open Sans",sans-serif;font-size:8px;line-height:10px;color:#222}
  .badge{width:50px;height:50px;border-radius:50%;background:#2f5d9a;margin-right:18px}
  .company strong{color:var(--green)}
  .company{width:284px}
  .contacts{width:240px}
  .footer-brand{margin-left:auto;text-align:right}
  .footer-brand .n{font-family:"Questrial",sans-serif;font-size:16px;line-height:18px}
  .footer-brand .u{font-size:9px;color:var(--red)}
</style>
</head>
<body>
  <svg class="corner" width="560" height="280" viewBox="0 0 560 280" role="img" aria-label="Red angular decorative corner">
    <defs>
      <linearGradient id="cornerFill" x1="0" y1="0" x2="1" y2="1">
        <stop offset="0" stop-color="var(--red)"/>
        <stop offset="1" stop-color="var(--wine)"/>
      </linearGradient>
    </defs>
    <polygon points="0,0 545,0 0,265" fill="url(#cornerFill)"/>
  </svg>

  <div class="brand">
    <div class="brand-name">LOOM STORE VAULT</div>
    <div class="brand-url">www.loomstorevault.net</div>
  </div>
  <div class="partner"><span class="partner-dot"></span>Corsa Data Services</div>

  <div class="title-bar">MODULO DI ATTIVAZIONE: CONTRATTO E CLIENTE</div>
  <p class="text" style="left:69px;top:276px">Con la presente si certifica l’avvenuta attivazione del contratto di<br>cancellazione sicura dei dati secondo le indicazioni che seguono.</p>

  <div class="box" style="top:332px;height:102px">Banca XXXXX soc. coop. a r. l.<br>P.IVA:<br>Contatto di riferimento: XXXX XXXX</div>

  <p class="text" style="left:69px;top:441px">Dati del Contratto</p>
  <div class="box" style="top:472px;height:166px">09956-29<br>Titolo: Banca XXXXX - 2015<br>Descrizone: Le attività di degaussing e triturazione saranno svolte in modo<br>centralizzato presso Corsa<br>Data Services.<br>Data inizio e fine: 2015-01-12</div>

  <p class="text" style="left:71px;top:649px">Utenti abilitati</p>
  <div class="box users" style="top:688px;height:46px;padding-top:10px"><span>XXXX XXXX</span><span>XXXXX@xxxx.com</span><span>Telefono:</span></div>

  <p class="text" style="left:72px;top:741px">Ulteriori PROVIDER Abilitati:<br>Il presente contratto è stato abilitata ai PROVIDER che seguono. Per ciascun<br>PROVIDER riferirsi al modulo P<br>di attivazione corrispondente.</p>
  <div class="box" style="top:858px;height:36px;padding-top:5px">Nessun ulteriore provider attivato.</div>

  <p class="text" style="left:74px;top:902px">Letto e accettato da:</p>
  <div class="box sign" style="left:65px;width:799px;top:934px;height:172px">
    <div class="col"><strong>CUSTOMER</strong><br><span style="line-height:32px">Data <span class="line"></span></span><br>Firma <span class="line"></span></div>
    <div class="col"><strong>LSV</strong><br>Marco Bellandi<br>Amministratore Unico<br>Corsa Data Services srl<br>Data <span class="line"></span><br><span style="line-height:36px">Firma <span class="line" style="width:150px"></span></span></div>
  </div>

  <p class="text" style="left:348px;top:1106px">Accordo di Segretezza</p>

  <div class="footer-rule"></div>
  <footer class="footer">
    <div class="badge"></div>
    <div class="company"><strong>CORSA DATA SERVICES s.r.l.</strong><br>Via dei Tigli 14 - 20100 Milano (MI)<br>IVA-VAT IT 00000000000 - c. fisc. 00000000000<br>reg. Imprese MI 00000000000<br>Cap. Soc. € 99.000,00 i.v.</div>
    <div class="contacts">tel +39 0200000100<br>fax +39 0200000199<br>email: info@corsadata.it<br>web: www.corsadata.it</div>
    <div class="footer-brand"><div class="n">LOOM STORE VAULT</div><div class="u">www.loomstorevault.net</div></div>
  </footer>
</body>
</html>
```